Ranked amongst the Best Colleges and Programs

the size of the ad is Full Page, with bleed*
8”x 10.75" plus 0.25" bleed'
you have two choices for the tagline .. please chose what ever you think will allow you to make a better ad.
The instructions on the brief are in red
I am looking for a hight quality modern ad to place in local weekly publications that will stand out .
I would like a ad that people will look at and say i would like to see what this ad is all about.
I apprecate creative work.
the ad should not be very crowded and the text should be able to be read.
if you decide to use people in the ad .. (you don't have to ) then it should be a male dressed in white shirt in and sports jacket.. or if you would like you can use a vector and then use male or female people.
please leave one inch on the bottom for the footer

Target Market(s)

potential middle class students from 23-35 years of age

Industry/Entity Type

education

Requirements
Must have
• .the " 98% employment rate" should stand out in the ad.. but should not be the main part of the ad
Nice to have
• creative
Should not have
• Should not be a very busy or crowded ad.. i prefer pictures of men but should be .. in a business suit .. that looks professional- white shirt

```html
<!DOCTYPE html>
<html lang="en">
<head>
<meta charset="utf-8">
<title>NBU Masters of Accounting – Full Page Ad</title>
<link rel="stylesheet" href="https://fonts.googleapis.com/css2?family=Montserrat:wght@300;400;500;600;700;800&display=swap">
<style>
  :root {
    --stage: #bdbdbd;
    --ink-dark: #262626;
    --ink-deep: #1a1a1a;
    --stone: #d3d3d3;
    --paper: #ffffff;
    --text-light: #ffffff;
    --text-dark: #161616;
    --rule-dark: #2b2b2b;
  }
  * { box-sizing: border-box; margin: 0; padding: 0; }
  html, body { width: 1013px; height: 1200px; overflow: hidden; }
  body {
    background: var(--stage);
    font-family: "Montserrat", Arial, sans-serif;
  }
  .ad {
    position: absolute;
    left: 59px; top: 0;
    width: 894px; height: 1200px;
    background: var(--paper);
    overflow: hidden;
  }
  .ad__art {
    position: absolute; left: 0; top: 0;
    width: 894px; height: 1088px;
    background: var(--ink-dark);
    overflow: hidden;
  }
  .ad__backdrop { position: absolute; inset: 0; }
  .ad__footer {
    position: absolute; left: 0; top: 1088px;
    width: 894px; height: 112px;
    background: var(--paper);
  }
  .portrait {
    position: absolute;
    left: 30px; top: 264px;
    width: 416px; height: 824px;
    border-radius: 190px 190px 0 0;
    background: linear-gradient(180deg, rgba(40,40,40,.35) 0%, rgba(20,20,20,.85) 35%, rgba(18,18,18,.95) 100%);
  }
  .headline {
    position: absolute; left: 30px; top: 22px;
    color: var(--text-light);
    text-transform: uppercase;
  }
  .headline__soft {
    display: block;
    font-weight: 500;
    font-size: 31.5px;
    letter-spacing: 2.5px;
    line-height: 36px;
  }
  .headline__strong {
    display: block;
    font-weight: 700;
    font-size: 47px;
    line-height: 44px;
    letter-spacing: 1px;
  }
  .headline__gap { display: block; height: 30px; }
  .program {
    position: absolute; left: 475px; top: 28px;
    height: 181px;
    border-left: 1.5px solid var(--text-light);
    padding-left: 28px;
    padding-top: 44px;
    color: var(--text-light);
  }
  .program__school {
    font-weight: 400;
    font-size: 19px;
    letter-spacing: 1.5px;
    line-height: 22px;
    margin-bottom: 12px;
  }
  .program__name {
    font-weight: 700;
    font-size: 28.5px;
    line-height: 28px;
    letter-spacing: 1px;
  }
  .rank-tag {
    position: absolute; left: 475px; top: 427px;
    width: 291px; height: 46px;
    border: 1.5px solid var(--rule-dark);
    border-radius: 4px;
    display: flex; align-items: center;
    padding-left: 26px;
    font-weight: 700;
    font-size: 25px;
    letter-spacing: 1px;
    color: var(--text-dark);
  }
  .rankings {
    position: absolute; left: 475px; top: 498px;
    width: 391px;
    border-left: 1.5px solid var(--rule-dark);
    color: var(--text-dark);
  }
  .rankings__item { padding: 8px 0 8px 28px; }
  .rankings__item + .rankings__item { border-top: 1.5px solid var(--rule-dark); }
  .rankings__list {
    font-weight: 400; font-size: 18.4px; letter-spacing: 1px; line-height: 22px;
  }
  .rankings__source {
    font-weight: 700; font-size: 24px; letter-spacing: 1.2px; line-height: 30px;
  }
  .stat-badge {
    position: absolute; left: 475px; top: 714px;
    width: 391px; height: 67px;
    background: var(--ink-deep);
    border-radius: 6px;
    box-shadow: 0 3px 8px rgba(0,0,0,.35);
    display: flex; align-items: center;
    padding-left: 28px;
    color: var(--text-light);
    font-weight: 700;
    font-size: 26.7px;
    letter-spacing: 1px;
  }
  .outcomes {
    position: absolute; left: 475px; top: 833px;
    height: 203px;
    border-left: 1.5px solid var(--text-light);
    padding-left: 28px;
    color: var(--text-light);
    font-weight: 300;
    font-size: 18.5px;
    line-height: 21.8px;
    letter-spacing: 1px;
  }
  .outcomes strong { font-weight: 700; }
</style>
</head>
<body>
  <main class="ad">
    <section class="ad__art">
      <svg class="ad__backdrop" width="894" height="1088" viewBox="0 0 894 1088" aria-hidden="true">
        <rect width="894" height="1088" fill="var(--ink-dark)"/>
        <polygon points="0,247 312,531 0,815" fill="var(--stone)"/>
        <polygon points="894,0 312,531 894,1061" fill="var(--stone)"/>
      </svg>

      <div class="portrait" role="img" aria-label="Smiling young businessman in a black suit, white shirt and striped tie, holding folders"></div>

      <h1 class="headline">
        <span class="headline__soft">A small investment</span>
        <span class="headline__strong">Today,</span>
        <span class="headline__gap"></span>
        <span class="headline__soft">A big difference</span>
        <span class="headline__strong">Tomorrow.</span>
      </h1>

      <div class="program">
        <p class="program__school">NBU-</p>
        <h2 class="program__name">Masters of<br>Accounting</h2>
      </div>

      <div class="rank-tag">Ranked amongst</div>

      <div class="rankings">
        <div class="rankings__item">
          <p class="rankings__list">Best Colleges</p>
          <p class="rankings__source">Velmora 2023</p>
        </div>
        <div class="rankings__item">
          <p class="rankings__list">Best Masters in Accounting</p>
          <p class="rankings__source">Scholavera 2023</p>
        </div>
      </div>

      <div class="stat-badge">98% Employment Rate</div>

      <p class="outcomes">
        <strong>NBU</strong><br>
        graduates<br>
        have gone on<br>
        to work in <strong>various</strong><br>
        <strong>high-quality jobs</strong><br>
        in top firms, earning<br>
        impressive six-figure<br>
        salaries as well as <strong>opening</strong><br>
        <strong>successful businesses</strong>.
      </p>
    </section>
    <footer class="ad__footer"></footer>
  </main>
</body>
</html>
```